TV Antenna Installation business needs a unique flyer

We need a simple but effective flyer design for our TV Aerial installation company based in Newcastle, NSW, Australia called Clearpeak TV & Aerial Svcs.
We are trying to target areas where there has been a new transmitter installed and most houses just require their aerial redirecting and tv's retuning.

Industry/Entity Type

Business

Requirements
Must have
• We would like the idea of a headline phrase such as " Poor TV reception……..now a thing from the past" or something similar & catchy.
Also "Did you know a new transmitter has been recently installed in your area, we can therefore now GUARANTEE 100% PERFECT PICTURE
Charges from only $95.
- Free 5 year warranty
- Free signal testing
- Free Onsite Quote
Phone 0452 736 205
Nice to have
• Other services include:

- New Installs
- Extra Points & repairs
- TV wall mounting/Home Cinema
- Pull down tall masts

Modern tv picture, see example uploaded

```html
<!DOCTYPE html>
<html lang="en">
<head>
<meta charset="utf-8">
<title>Clearpeak TV &amp; Aerial Svcs – Flyer</title>
<link rel="stylesheet" href="https://fonts.googleapis.com/css2?family=Questrial&family=Montserrat:wght@700&family=Pathway+Gothic+One&family=Arimo&family=Roboto+Condensed:wght@700&display=swap">
<style>
  :root {
    --purple: #8a4aa3;
    --lavender: #c3c1e6;
    --orange: #ff6600;
    --green: #3e8d46;
    --ink: #333333;
    --white: #ffffff;
    --frame: #7a7a7a;
  }
  * { margin: 0; padding: 0; box-sizing: border-box; }
  html, body { width: 906px; height: 1200px; overflow: hidden; background: var(--white); }
  .flyer { position: relative; width: 906px; height: 1200px; overflow: hidden; background: var(--white); }
  .shapes { position: absolute; left: 0; top: 0; width: 906px; height: 1200px; }
  .abs { position: absolute; white-space: nowrap; }

  .brand-title {
    left: 0; width: 906px; top: 22px; text-align: center;
    font-family: "Questrial", sans-serif; font-size: 47px; line-height: 56px;
    color: var(--white); letter-spacing: 1px;
  }
  .tagline-text { font-family: "Pathway Gothic One", sans-serif; font-size: 46px; fill: var(--white); }

  .headline {
    left: 0; width: 906px; top: 558px; text-align: center;
    font-family: "Montserrat", sans-serif; font-weight: 700; font-size: 30px; line-height: 43px;
    color: var(--ink); white-space: normal;
  }
  .headline .guarantee { color: var(--green); }

  .price-tag {
    left: 25px; top: 716px;
    font-family: "Questrial", sans-serif; font-size: 34px; line-height: 44px; color: var(--white);
  }
  .perks, .services { list-style: none; font-family: "Questrial", sans-serif; color: var(--ink); }
  .perks { left: 92px; top: 795px; font-size: 24px; }
  .perks li { height: 34px; line-height: 30px; }
  .services { left: 457px; top: 1006px; font-size: 24px; }
  .services li { height: 35px; line-height: 32px; }

  .call-label {
    left: 440px; width: 466px; top: 738px; text-align: center;
    font-family: "Arimo", sans-serif; font-size: 66px; line-height: 76px; color: var(--white);
  }
  .call-number {
    left: 460px; width: 446px; top: 806px; text-align: center;
    font-family: "Roboto Condensed", sans-serif; font-weight: 700; font-size: 80px; line-height: 88px;
    color: var(--white);
  }
  .services-heading {
    left: 423px; top: 917px;
    font-family: "Questrial", sans-serif; font-size: 42px; line-height: 50px; color: var(--white);
  }

  .promo-box {
    left: 19px; top: 956px; width: 347px; height: 196px;
    border: 2px solid var(--frame); border-radius: 12px; background: var(--white);
    text-align: center; font-family: "Roboto Condensed", sans-serif; font-weight: 700; color: var(--orange);
    white-space: normal;
  }
  .promo-box .promo-ask { font-size: 31px; line-height: 36px; margin-top: 8px; }
  .promo-box .promo-cta { font-size: 58px; line-height: 66px; }
</style>
</head>
<body>
<div class="flyer">
  <svg class="shapes" viewBox="0 0 981 1300" width="906" height="1200" aria-hidden="false">
    <defs>
      <polygon id="star" points="0,-12 3.5,-4 12,-3.7 5.4,2 7.4,10.5 0,6 -7.4,10.5 -5.4,2 -12,-3.7 -3.5,-4" fill="var(--green)"/>
    </defs>

    <!-- title ribbon -->
    <polygon points="10,54 45,15 75,15 75,93 45,93" fill="var(--lavender)"/>
    <polygon points="971,54 936,15 906,15 906,93 936,93" fill="var(--lavender)"/>
    <polygon points="22,54 52,15 929,15 959,54 929,93 52,93" fill="var(--purple)"/>

    <!-- hero chevron -->
    <polygon points="0,165 268,165 290,178 455,370 290,565 268,578 0,578" fill="var(--lavender)"/>
    <polygon points="268,165 318,165 510,370 318,578 268,578 455,370" fill="var(--purple)"/>

    <!-- tagline ribbon -->
    <path d="M0,178 Q480,118 981,128 L981,190 Q480,182 0,250 Z" fill="var(--orange)"/>
    <path id="taglinePath" d="M22,238 Q480,168 960,170" fill="none"/>
    <text class="tagline-text"><textPath href="#taglinePath">Poor TV reception……..now a thing from the past !</textPath></text>

    <!-- tv illustrations -->
    <g role="img" aria-label="Retro TV with a weak, noisy signal wave on screen">
      <rect x="72" y="258" width="168" height="282" rx="8" fill="#b55a2e" opacity="0.85"/>
    </g>
    <g role="img" aria-label="Retro TV showing a crisp photo of a red rose">
      <rect x="566" y="188" width="242" height="412" rx="8" fill="#c3502c" opacity="0.9"/>
    </g>

    <!-- price ribbon -->
    <polygon points="0,760 425,760 470,799 425,838 0,838" fill="var(--lavender)"/>
    <polygon points="0,760 420,760 455,799 420,838 0,838" fill="var(--purple)"/>

    <!-- call panel -->
    <polygon points="425,963 600,795 981,795 981,963" fill="var(--orange)"/>

    <!-- services ribbon -->
    <polygon points="402,1020 442,982 470,982 470,1058 442,1058" fill="var(--lavender)"/>
    <polygon points="414,1020 452,982 981,982 981,1058 452,1058" fill="var(--purple)"/>

    <!-- bullet stars -->
    <use href="#star" x="77" y="877"/>
    <use href="#star" x="77" y="913"/>
    <use href="#star" x="77" y="951"/>
    <use href="#star" x="470" y="1107"/>
    <use href="#star" x="470" y="1143"/>
    <use href="#star" x="470" y="1181"/>
    <use href="#star" x="470" y="1222"/>
  </svg>

  <h1 class="abs brand-title">Clearpeak TV &amp; Aerial Svcs</h1>

  <p class="abs headline">Did you know a new transmitter has been recently<br>installed in your area, we can therefore now<br><span class="guarantee">GUARANTEE 100% PERFECT PICTURE</span> !</p>

  <p class="abs price-tag">Charges from only $95</p>
  <ul class="abs perks">
    <li>Free 5 year warranty</li>
    <li>Free signal testing</li>
    <li>Free Onsite Quote</li>
  </ul>

  <p class="abs call-label">Call Now</p>
  <p class="abs call-number">0452 736 205</p>

  <h2 class="abs services-heading">Other services include</h2>
  <ul class="abs services">
    <li>New Installs</li>
    <li>Extra Outlets &amp; repairs</li>
    <li>TV wall mounting / Home Cinema</li>
    <li>Pull down tall masts</li>
  </ul>

  <div class="abs promo-box">
    <p class="promo-ask">Want Clear Reception?</p>
    <p class="promo-cta">Call Us Today</p>
    <p class="promo-cta">&amp; Feel Great !</p>
  </div>
</div>
</body>
</html>
```